UX revamp for crypto platform mobile app

re-design the assets of a mobile app to give them a sleek, current and modern feel see reference below.
The current app has 3 main menus with subfunctions:
Wallet: Send - Receive - Top-up with shortcut to other main menus
Talents: User can support talent and see his support
Rewards: User can purchase rewards from Talents - Clubs - Plumtoken

Target Market(s)

Youth fans of sports and entertainment

Industry/Entity Type

Blockchain

Colors

Designer to choose colors to be used in the design.

Requirements
Must have
• Modern - sleek - stylish - current trends design
Nice to have
• Need to be clean design
Should not have
• too dark and heavy

```html
<!DOCTYPE html>
<html lang="en">
<head>
<meta charset="utf-8">
<title>Plumtoken – Mobile App UI</title>
<link rel="stylesheet" href="https://fonts.googleapis.com/css2?family=Manrope:wght@400;500;600;700;800&display=swap">
<style>
:root{
  --orange:#f39322;
  --orange-soft:#fbd3a3;
  --ink:#1d1d1f;
  --blue:#2c5a85;
  --grey:#8a8f96;
  --line:#dcdcdc;
  --screen-bg:#f1f1f1;
  --card:#ffffff;
  --page:#ffffff;
  --violet:#7b7fe0;
}
*{box-sizing:border-box;margin:0;padding:0}
html,body{width:1200px;height:2908px;overflow:hidden;background:var(--page);font-family:"Manrope",sans-serif;color:var(--ink)}
.canvas{position:relative;width:1200px;height:2908px}

.brand{position:absolute;top:92px;left:477px;display:flex;align-items:center;gap:24px}
.brand-dot{width:96px;height:96px;border-radius:50%;background:var(--orange)}
.brand-name{font-size:22px;font-weight:600;color:var(--orange)}
.version{position:absolute;top:2770px;left:0;width:1200px;text-align:center;font-size:25px;font-weight:500;color:var(--orange)}

.screen{position:absolute;width:238px}
.screen-title{height:20px;line-height:20px;margin-bottom:33px;text-align:center;font-size:17px;font-weight:600}
.phone{position:relative;width:238px;height:508px;border:2px solid var(--orange);border-radius:10px;overflow:hidden;background:var(--screen-bg);display:flex;flex-direction:column}
.phone.white{background:#fff}

.hdr{height:62px;flex:none;background:var(--orange);position:relative;color:#fff}
.hdr-title{position:absolute;left:0;right:0;bottom:12px;text-align:center;font-size:11px;font-weight:700}
.hdr svg{position:absolute;bottom:12px;width:13px;height:13px}
.hdr .gear{right:12px}
.hdr .back{left:12px}

.body{flex:1;position:relative;padding:8px 10px 0;overflow:hidden}
.nav{height:40px;flex:none;background:#fff;display:flex;border-top:1px solid var(--line)}
.nav-item{flex:1;display:flex;flex-direction:column;align-items:center;justify-content:center;gap:3px;font-size:7.5px;font-weight:700;color:var(--ink)}
.nav-item svg{width:13px;height:13px}
.nav-item.active{color:var(--orange);border-top:2px solid var(--orange)}

.balance-card{background:var(--card);box-shadow:0 2px 6px rgba(0,0,0,.12);text-align:center;padding:12px 0 10px;margin-bottom:14px}
.balance-label{font-size:7.5px;color:var(--blue)}
.balance-value{font-size:15px;font-weight:700;color:var(--orange);margin:5px 0 4px}
.balance-change{font-size:7px;color:var(--grey)}
.section-label{font-size:9px;font-weight:700;margin:0 0 8px}
.transfer{background:var(--card);display:flex;align-items:center;height:38px;margin-bottom:8px;padding:0 10px;font-size:7px}
.transfer .col{flex:1;display:flex;flex-direction:column;gap:4px}
.transfer .col.right{text-align:right}
.transfer .divider{width:1px;height:20px;background:var(--line)}
.muted{color:var(--grey)}
.date{color:var(--blue);font-weight:600}
.amount{color:var(--orange);font-weight:600}

.fab{position:absolute;right:12px;width:30px;height:30px;border-radius:50%;background:var(--orange);display:flex;align-items:center;justify-content:center}
.fab svg{width:13px;height:13px}
.fab.small{width:26px;height:26px;right:14px}
.fab.small svg{width:11px;height:11px}

.onboard{flex:1;display:flex;flex-direction:column;align-items:center}
.mini-brand{display:flex;align-items:center;gap:6px;margin-top:112px;font-size:11px;font-weight:600;color:var(--orange)}
.mini-brand span.dot{width:22px;height:22px;border-radius:50%;background:var(--orange)}
.prompt{font-size:8px;font-weight:500;text-align:center}
.pin{display:flex;gap:7px;justify-content:center}
.pin span{width:30px;height:30px;border:1px solid var(--orange);background:#fff}
.btn{background:var(--orange);color:#fff;font-size:8px;font-weight:700;display:flex;align-items:center;justify-content:center;width:80px;height:28px}

.overlay{position:absolute;left:0;right:0;top:62px;height:252px;background:rgba(40,40,40,.55)}
.sheet{position:absolute;left:0;right:0;bottom:0;height:192px;background:#fff;padding:14px 12px}
.sheet-title{font-size:8px;font-weight:600;margin-bottom:12px}
.option{display:flex;align-items:center;gap:12px;background:var(--screen-bg);height:34px;padding:0 10px;margin-bottom:10px;font-size:8px;font-weight:700;color:var(--blue)}
.option .coin{width:14px;height:14px;border-radius:50%}

.send{flex:1;display:flex;flex-direction:column;align-items:center;padding:26px 14px 0;text-align:center}
.send .field{width:210px;height:30px;border:1px solid var(--orange);background:var(--screen-bg);margin:10px 0 34px}
.kv-label{font-size:8.5px;font-weight:600}
.kv-value{font-size:7.5px;font-weight:600;color:var(--blue);margin:8px 0 30px}
.kv-value.orange{color:var(--orange)}

.tabs{display:flex;justify-content:center;gap:6px;margin:6px 0 14px}
.tab{font-size:8px;font-weight:600;padding:0 14px;height:24px;line-height:24px;border-radius:12px}
.tab.active{background:var(--orange);color:#fff}
.letter{font-size:9px;font-weight:700;margin:0 0 8px 2px}
.talent{display:flex;align-items:center;background:var(--card);height:44px;padding:0 10px;margin-bottom:10px;gap:9px}
.avatar{width:22px;height:22px;border-radius:50%;background:linear-gradient(135deg,#6b4a36,#c99a72);flex:none}
.talent-text{flex:1;display:flex;flex-direction:column;gap:3px}
.talent-name{font-size:8px;font-weight:600;color:var(--blue)}
.talent-role{font-size:6.5px;font-weight:600}
.flag{width:17px;height:12px;flex:none}
.flag-ke{background:linear-gradient(#1b1b1b 0 30%,#fff 30% 35%,#c8202f 35% 65%,#fff 65% 70%,#2d7a3a 70%)}
.flag-us{background:linear-gradient(90deg,#2c3f7a 0 42%,transparent 42%) top/100% 55% no-repeat,repeating-linear-gradient(#c8202f 0 1.7px,#fff 1.7px 3.4px)}
.flag-en{background:linear-gradient(90deg,transparent 42%,#c8202f 42% 58%,transparent 58%),linear-gradient(#fff 40%,#c8202f 40% 60%,#fff 60%)}
.flag-tr{background:radial-gradient(circle at 42% 50%,#fff 0 3px,transparent 3.2px),#d8262f}

.profile-card{background:var(--card);text-align:center;padding:0 0 10px;margin:-2px 0 14px}
.profile-avatar{width:36px;height:36px;border-radius:50%;background:linear-gradient(135deg,#4a3024,#b98460);margin:0 auto 2px;position:relative;top:-2px}
.profile-wrap{position:relative;padding-top:12px}
.profile-card .talent-name{font-size:8.5px}
.profile-card .flag{display:inline-block;margin-top:5px}
.stat{display:flex;align-items:center;background:var(--card);height:32px;padding:0 10px;margin-bottom:10px;font-size:7px;font-weight:600}
.stat .k{flex:1;color:var(--blue)}
.stat .divider{width:1px;height:18px;background:var(--line);margin-right:10px}
.stat .v{flex:1;text-align:right;color:var(--orange)}
.stat .v.plain{color:var(--grey)}
.buy-bar{display:flex;height:40px;padding:5px 10px;gap:4px;background:var(--screen-bg)}
.buy-bar .input{flex:1;background:#fff;border:1px solid var(--line);font-size:7px;color:var(--grey);display:flex;align-items:center;padding-left:8px}
.buy-bar .btn{width:66px;height:auto}

.reward{display:flex;align-items:center;gap:10px;background:var(--card);height:40px;padding:0 12px;margin-bottom:10px;font-size:7.5px;font-weight:600;color:var(--blue)}
.reward svg{width:12px;height:12px;flex:none}

.setting{display:flex;align-items:center;gap:12px;background:var(--card);height:34px;padding:0 12px;margin:0 4px 13px;font-size:7.5px;font-weight:600;color:var(--blue)}
.setting svg{width:12px;height:12px}
</style>
</head>
<body>
<svg width="0" height="0" style="position:absolute" aria-hidden="true">
  <symbol id="i-gear" viewBox="0 0 24 24"><path fill="currentColor" d="M12 8.5a3.5 3.5 0 1 0 0 7 3.5 3.5 0 0 0 0-7zm9 5.2v-3.4l-2.6-.5a7 7 0 0 0-.7-1.6l1.5-2.2-2.4-2.4-2.2 1.5a7 7 0 0 0-1.6-.7L12.5 2h-3.4l-.5 2.6a7 7 0 0 0-1.6.7L4.8 3.8 2.4 6.2l1.5 2.2a7 7 0 0 0-.7 1.6L.6 10.3v3.4l2.6.5c.2.6.4 1.1.7 1.6l-1.5 2.2 2.4 2.4 2.2-1.5c.5.3 1 .5 1.6.7l.5 2.6h3.4l.5-2.6c.6-.2 1.1-.4 1.6-.7l2.2 1.5 2.4-2.4-1.5-2.2c.3-.5.5-1 .7-1.6z" transform="translate(1 0)"/></symbol>
  <symbol id="i-back" viewBox="0 0 24 24"><path d="M20 12H5M11 5l-7 7 7 7" fill="none" stroke="currentColor" stroke-width="2.4" stroke-linecap="round" stroke-linejoin="round"/></symbol>
  <symbol id="i-wallet" viewBox="0 0 24 24"><path d="M3 7h16a2 2 0 0 1 2 2v9a2 2 0 0 1-2 2H5a2 2 0 0 1-2-2zM3 7l12-4v4M16 13h2" fill="none" stroke="currentColor" stroke-width="2" stroke-linejoin="round"/></symbol>
  <symbol id="i-star" viewBox="0 0 24 24"><path d="M12 3l2.8 5.8 6.2.9-4.5 4.4 1.1 6.2L12 17.4l-5.6 2.9 1.1-6.2L3 9.7l6.2-.9z" fill="none" stroke="currentColor" stroke-width="2" stroke-linejoin="round"/></symbol>
  <symbol id="i-trophy" viewBox="0 0 24 24"><path d="M7 3h10v6a5 5 0 0 1-10 0zM7 5H3v2a4 4 0 0 0 4 4M17 5h4v2a4 4 0 0 1-4 4M12 14v4M8 21h8M9 18h6" fill="none" stroke="currentColor" stroke-width="2" stroke-linejoin="round"/></symbol>
  <symbol id="i-plus" viewBox="0 0 24 24"><path d="M12 4v16M4 12h16" stroke="#fff" stroke-width="3" stroke-linecap="round"/></symbol>
  <symbol id="i-close" viewBox="0 0 24 24"><path d="M6 6l12 12M18 6L6 18" stroke="#fff" stroke-width="3" stroke-linecap="round"/></symbol>
  <symbol id="i-sendplane" viewBox="0 0 24 24"><path d="M3 11l18-8-8 18-2-8z" fill="none" stroke="#fff" stroke-width="2.4" stroke-linejoin="round"/></symbol>
  <symbol id="i-topup" viewBox="0 0 24 24"><path d="M4 5h16v5H4zM7 10v9h10v-9M12 12v5M10 15l2 2 2-2" fill="none" stroke="#fff" stroke-width="2.2" stroke-linejoin="round"/></symbol>
  <symbol id="i-lock" viewBox="0 0 24 24"><path d="M6 11h12v10H6zM8 11V7a4 4 0 0 1 8 0v4" fill="none" stroke="currentColor" stroke-width="2.2"/></symbol>
  <symbol id="i-shield" viewBox="0 0 24 24"><path d="M12 2l8 3v6c0 5-3.5 9-8 11-4.5-2-8-6-8-11V5z" fill="currentColor"/><path d="M8.5 12l2.5 2.5 4.5-5" fill="none" stroke="#fff" stroke-width="2"/></symbol>
  <symbol id="i-bank" viewBox="0 0 24 24"><path d="M3 9l9-6 9 6zM5 10v8M9.5 10v8M14.5 10v8M19 10v8M3 21h18" fill="none" stroke="currentColor" stroke-width="2" stroke-linejoin="round"/></symbol>
  <symbol id="i-user" viewBox="0 0 24 24"><circle cx="12" cy="8" r="4.5" fill="currentColor"/><path d="M3 22a9 8 0 0 1 18 0z" fill="currentColor"/></symbol>
</svg>

<main class="canvas">
  <header class="brand">
    <span class="brand-dot"></span>
    <span class="brand-name">Plumtoken</span>
  </header>

  <!-- Row 1 -->
  <section class="screen" style="left:144px;top:280px">
    <h2 class="screen-title">Onboarding</h2>
    <div class="phone white">
      <div class="onboard">
        <div class="mini-brand"><span class="dot"></span>Plumtoken</div>
        <p class="prompt" style="margin-top:118px">Enter the pin code you recieved</p>
        <div class="pin" style="margin-top:20px"><span></span><span></span><span></span><span></span></div>
        <div class="btn" style="margin-top:126px">Login</div>
      </div>
    </div>
  </section>

  <section class="screen" style="left:462px;top:280px">
    <h2 class="screen-title">Balance</h2>
    <div class="phone">
      <div class="hdr"><span class="hdr-title">Balance</span><svg class="gear"><use href="#i-gear"/></svg></div>
      <div class="body">
        <div class="balance-card"><p class="balance-label">Current Balance</p><p class="balance-value">83.8598</p><p class="balance-change">(2.27%)</p></div>
        <p class="section-label">Transfers</p>
        <div class="transfer"><div class="col"><span class="muted">Sent</span><span class="date">5 days ago</span></div><span class="divider"></span><div class="col right"><span class="muted">Amount</span><span class="amount">-10 PLM</span></div></div>
        <div class="transfer"><div class="col"><span class="muted">Sent</span><span class="date">12 days ago</span></div><span class="divider"></span><div class="col right"><span class="muted">Amount</span><span class="amount">-10 PLM</span></div></div>
        <div class="transfer"><div class="col"><span class="muted">Sent</span><span class="date">November 22</span></div><span class="divider"></span><div class="col right"><span class="muted">Amount</span><span class="amount">-10 PLM</span></div></div>
        <div class="transfer"><div class="col"><span class="muted">Sent</span><span class="date">May 22</span></div><span class="divider"></span><div class="col right"><span class="muted">Amount</span><span class="amount">-10 PLM</span></div></div>
        <div class="transfer"><div class="col"><span class="muted">Sent</span><span class="date">August 12</span></div><span class="divider"></span><div class="col right"><span class="muted">Amount</span><span class="amount">-10 PLM</span></div></div>
      </div>
      <div class="fab" style="bottom:48px"><svg><use href="#i-plus"/></svg></div>
      <nav class="nav"><div class="nav-item active"><svg><use href="#i-wallet"/></svg>Balance</div><div class="nav-item"><svg><use href="#i-star"/></svg>Talent</div><div class="nav-item"><svg><use href="#i-trophy"/></svg>Rewards</div></nav>
    </div>
  </section>

  <section class="screen" style="left:779px;top:280px">
    <h2 class="screen-title">Balance - FAB</h2>
    <div class="phone">
      <div class="hdr"><span class="hdr-title">Balance</span><svg class="gear"><use href="#i-gear"/></svg></div>
      <div class="body">
        <div class="balance-card"><p class="balance-label">Current Balance</p><p class="balance-value">83.8598</p><p class="balance-change">(2.27%)</p></div>
        <p class="section-label">Transfers</p>
        <div class="transfer"><div class="col"><span class="muted">Sent</span><span class="date">5 days ago</span></div><span class="divider"></span><div class="col right"><span class="muted">Amount</span><span class="amount">-10 PLM</span></div></div>
        <div class="transfer"><div class="col"><span class="muted">Sent</span><span class="date">12 days ago</span></div><span class="divider"></span><div class="col right"><span class="muted">Amount</span><span class="amount">-10 PLM</span></div></div>
        <div class="transfer"><div class="col"><span class="muted">Sent</span><span class="date">November 22</span></div><span class="divider"></span><div class="col right"><span class="muted">Amount</span><span class="amount">-10 PLM</span></div></div>
        <div class="transfer"><div class="col"><span class="muted">Sent</span><span class="date">May 22</span></div><span class="divider"></span><div class="col right"><span class="muted">Amount</span><span class="amount">-10 PLM</span></div></div>
        <div class="transfer"><div class="col"><span class="muted">Sent</span><span class="date">August 12</span></div><span class="divider"></span><div class="col right"><span class="muted">Amount</span><span class="amount">-10 PLM</span></div></div>
      </div>
      <div class="fab small" style="bottom:128px"><svg><use href="#i-sendplane"/></svg></div>
      <div class="fab small" style="bottom:92px"><svg><use href="#i-topup"/></svg></div>
      <div class="fab" style="bottom:48px"><svg><use href="#i-close"/></svg></div>
      <nav class="nav"><div class="nav-item active"><svg><use href="#i-wallet"/></svg>Balance</div><div class="nav-item"><svg><use href="#i-star"/></svg>Talent</div><div class="nav-item"><svg><use href="#i-trophy"/></svg>Rewards</div></nav>
    </div>
  </section>

  <!-- Row 2 -->
  <section class="screen" style="left:144px;top:868px">
    <h2 class="screen-title">Currency Selection</h2>
    <div class="phone">
      <div class="hdr"><span class="hdr-title">Balance</span><svg class="gear"><use href="#i-gear"/></svg></div>
      <div class="body">
        <div class="balance-card"><p class="balance-label">Current Balance</p><p class="balance-value">83.8598</p><p class="balance-change">(2.27%)</p></div>
        <p class="section-label">Transfers</p>
        <div class="transfer"><div class="col"><span class="muted">Sent</span><span class="date">5 days ago</span></div><span class="divider"></span><div class="col right"><span class="muted">Amount</span><span class="amount">-10 PLM</span></div></div>
        <div class="transfer"><div class="col"><span class="muted">Sent</span><span class="date">12 days ago</span></div><span class="divider"></span><div class="col right"><span class="muted">Amount</span><span class="amount">-10 PLM</span></div></div>
      </div>
      <div class="overlay"></div>
      <div class="sheet">
        <p class="sheet-title">Select the currency:</p>
        <div class="option"><span class="coin" style="background:var(--orange)"></span>Plumtoken</div>
        <div class="option"><span class="coin" style="background:var(--violet)"></span>Vaultchain</div>
      </div>
    </div>
  </section>

  <section class="screen" style="left:462px;top:868px">
    <h2 class="screen-title">Get PLM - Send</h2>
    <div class="phone white">
      <div class="hdr"><svg class="back"><use href="#i-back"/></svg><span class="hdr-title">Get PLM</span></div>
      <div class="send">
        <p class="kv-label">Enter the amount:</p>
        <div class="field"></div>
        <p class="kv-label">Target Address</p>
        <p class="kv-value">0cjmudadadmcctxt54254532mcl</p>
        <p class="kv-label" style="margin-top:-6px">My Address</p>
        <p class="kv-value">0cjmunsansalatxt542ue9uecliko</p>
        <p class="kv-label" style="margin-top:-6px">PLM VALUE</p>
        <p class="kv-value orange" style="margin-bottom:22px">10.000 PLM</p>
        <p class="prompt">Enter the pin code you recieved</p>
        <div class="pin" style="margin-top:12px"><span></span><span></span><span></span><span></span></div>
        <div class="btn" style="margin-top:42px">Send</div>
      </div>
    </div>
  </section>

  <section class="screen" style="left:779px;top:868px">
    <h2 class="screen-title">Talents</h2>
    <div class="phone">
      <div class="hdr"><span class="hdr-title">Talent</span><svg class="gear"><use href="#i-gear"/></svg></div>
      <div class="body">
        <div class="tabs"><span class="tab active">PlumStream</span><span class="tab">My Team</span></div>
        <p class="letter">A</p>
        <div class="talent"><span class="avatar" role="img" aria-label="Portrait photo of Tobin Garza"></span><div class="talent-text"><span class="talent-name">Tobin Garza</span><span class="talent-role">Basketball</span></div><span class="flag flag-ke"></span></div>
        <div class="talent"><span class="avatar" role="img" aria-label="Portrait photo of Maren Colby"></span><div class="talent-text"><span class="talent-name">Maren Colby</span><span class="talent-role">Singer</span></div><span class="flag flag-us"></span></div>
        <p class="letter">B</p>
        <div class="talent"><span class="avatar" role="img" aria-label="Portrait photo of Clarice Benning"></span><div class="talent-text"><span class="talent-name">Clarice Benning</span><span class="talent-role">Actress</span></div><span class="flag flag-en"></span></div>
        <div class="talent"><span class="avatar" role="img" aria-label="Portrait photo of Alina Whitford"></span><div class="talent-text"><span class="talent-name">Alina Whitford</span><span class="talent-role">Singer</span></div><span class="flag flag-tr"></span></div>
      </div>
      <nav class="nav"><div class="nav-item"><svg><use href="#i-wallet"/></svg>Balance</div><div class="nav-item active"><svg><use href="#i-star"/></svg>Talent</div><div class="nav-item"><svg><use href="#i-trophy"/></svg>Rewards</div></nav>
    </div>
  </section>

  <!-- Row 3 -->
  <section class="screen" style="left:144px;top:1457px">
    <h2 class="screen-title">Talents - My team</h2>
    <div class="phone">
      <div class="hdr"><span class="hdr-title">Talent</span><svg class="gear"><use href="#i-gear"/></svg></div>
      <div class="body">
        <div class="tabs"><span class="tab">PlumStream</span><span class="tab active">My Team</span></div>
        <p class="letter">A</p>
        <div class="talent"><span class="avatar" role="img" aria-label="Portrait photo of Tobin Garza"></span><div class="talent-text"><span class="talent-name">Tobin Garza</span><span class="talent-role">Basketball</span></div><span class="flag flag-ke"></span></div>
        <div class="talent"><span class="avatar" role="img" aria-label="Portrait photo of Maren Colby"></span><div class="talent-text"><span class="talent-name">Maren Colby</span><span class="talent-role">Singer</span></div><span class="flag flag-us"></span></div>
        <p class="letter">B</p>
        <div class="talent"><span class="avatar" role="img" aria-label="Portrait photo of Clarice Benning"></span><div class="talent-text"><span class="talent-name">Clarice Benning</span><span class="talent-role">Actress</span></div><span class="flag flag-en"></span></div>
        <div class="talent"><span class="avatar" role="img" aria-label="Portrait photo of Alina Whitford"></span><div class="talent-text"><span class="talent-name">Alina Whitford</span><span class="talent-role">Singer</span></div><span class="flag flag-tr"></span></div>
      </div>
      <nav class="nav"><div class="nav-item"><svg><use href="#i-wallet"/></svg>Balance</div><div class="nav-item active"><svg><use href="#i-star"/></svg>Talent</div><div class="nav-item"><svg><use href="#i-trophy"/></svg>Rewards</div></nav>
    </div>
  </section>

  <section class="screen" style="left:462px;top:1457px">
    <h2 class="screen-title">Profile</h2>
    <div class="phone">
      <div class="hdr"><svg class="back"><use href="#i-back"/></svg><span class="hdr-title">Profile</span></div>
      <div class="body profile-wrap">
        <div class="profile-avatar" role="img" aria-label="Portrait photo of Maren Colby"></div>
        <div class="profile-card">
          <div style="height:4px"></div>
          <p class="talent-name">Maren Colby</p>
          <p class="talent-role" style="margin-top:3px">Singer</p>
          <span class="flag flag-us"></span>
        </div>
        <div class="stat"><span class="k">Profession</span><span class="divider"></span><span class="v plain">Actress</span></div>
        <div class="stat"><span class="k">Released</span><span class="divider"></span><span class="v">0.00159%</span></div>
        <div class="stat"><span class="k">USD value</span><span class="divider"></span><span class="v">350000000</span></div>
        <div class="stat"><span class="k">PLM value</span><span class="divider"></span><span class="v">174765900</span></div>
        <div class="stat"><span class="k">PLM commit</span><span class="divider"></span><span class="v">305.0</span></div>
        <div class="stat"><span class="k">Available</span><span class="divider"></span><span class="v">3006</span></div>
      </div>
      <div class="buy-bar"><div class="input">Enter the amount</div><div class="btn">Get PLM</div></div>
    </div>
  </section>

  <section class="screen" style="left:779px;top:1457px">
    <h2 class="screen-title">Rewards</h2>
    <div class="phone">
      <div class="hdr"><span class="hdr-title">Rewards</span><svg class="gear"><use href="#i-gear"/></svg></div>
      <div class="body">
        <div class="tabs"><span class="tab active">Talents</span><span class="tab">Team</span><span class="tab">PLM</span></div>
        <p class="letter">F</p>
        <div class="reward"><svg style="color:var(--orange)"><use href="#i-trophy"/></svg>Feed Post - A Osterlund</div>
        <div class="reward"><svg style="color:var(--orange)"><use href="#i-trophy"/></svg>Feed Post - Galvin r</div>
        <p class="letter">T</p>
        <div class="reward"><svg style="color:var(--orange)"><use href="#i-trophy"/></svg>Chirp - A Osterlund</div>
      </div>
      <nav class="nav"><div class="nav-item"><svg><use href="#i-wallet"/></svg>Balance</div><div class="nav-item"><svg><use href="#i-star"/></svg>Talent</div><div class="nav-item active"><svg><use href="#i-trophy"/></svg>Rewards</div></nav>
    </div>
  </section>

  <!-- Row 4 -->
  <section class="screen" style="left:310px;top:2045px">
    <h2 class="screen-title">Rewards - Team Rewards</h2>
    <div class="phone">
      <div class="hdr"><span class="hdr-title">Rewards</span><svg class="gear"><use href="#i-gear"/></svg></div>
      <div class="body">
        <div class="tabs"><span class="tab">Talents</span><span class="tab active">Team</span><span class="tab">PLM</span></div>
        <p class="letter">X</p>
        <div class="reward"><svg style="color:var(--orange)"><use href="#i-trophy"/></svg>XX - Team -Rewards</div>
      </div>
      <nav class="nav"><div class="nav-item"><svg><use href="#i-wallet"/></svg>Balance</div><div class="nav-item"><svg><use href="#i-star"/></svg>Talent</div><div class="nav-item active"><svg><use href="#i-trophy"/></svg>Rewards</div></nav>
    </div>
  </section>

  <section class="screen" style="left:627px;top:2045px">
    <h2 class="screen-title">Settings</h2>
    <div class="phone">
      <div class="hdr"><svg class="back"><use href="#i-back"/></svg><span class="hdr-title">Settings</span></div>
      <div class="body" style="padding-top:24px">
        <div class="setting"><svg style="color:var(--orange)"><use href="#i-lock"/></svg>Change Pin</div>
        <div class="setting"><svg style="color:var(--orange)"><use href="#i-shield"/></svg>View Private Key</div>
        <div class="setting"><svg style="color:var(--orange)"><use href="#i-bank"/></svg>Plumtoken institute</div>
        <div class="setting"><svg style="color:var(--orange)"><use href="#i-user"/></svg>Logout</div>
      </div>
    </div>
  </section>

  <p class="version">version 1.02</p>
</main>
</body>
</html>
```